Maren Tolliver Luxury Wellness Profile Booklet

I am a luxury wellness property agent and would like to create my personal profile booklet. I want this to feel luxurious, minimalist, informative and the philosophy behind wellness and property the cPAGE 1 — THE COVER

Very minimal.

MAREN TOLLIVER

LUXURY WELLNESS PROPERTY

PROPERTY • WELLNESS • LIFESTYLE

Keel Ashby Coastline Group

Large photograph of you — preferably walking through a beautiful waterfront property or standing naturally within an architectural setting.

At the bottom:

Hope Island • Sanctuary Cove • Helensvale

Small Keel Ashby logo.

PAGE 2 — THE OPENING STATEMENT

A beautiful full-page lifestyle photograph.

Overlaid:

WHERE PROPERTY
MEETS WELLBEING

“A home is more than an address. It is the environment in which life unfolds.”

Then a short introduction:

Opening Profile

I believe the most exceptional properties are not defined simply by their architecture, address or price.

They are defined by how they make you feel.

Natural light. Water views. Privacy. Green space. Indoor-outdoor living. A place to unwind, entertain, recharge and reconnect.

My approach to luxury property brings these elements together — combining strategic real estate expertise with a genuine understanding of wellness, lifestyle and the way people want to live today.

Because when we understand the lifestyle behind the property, we can create a more compelling story around it.

PAGE 3 — MEET MAREN

Large portrait of you on one side.

Other side:

MEET MAREN

20+ YEARS OF PROPERTY EXPERIENCE

Commercial
Residential
Project Sales
Luxury & Lifestyle Property

Then:

About Maren

With more than 20 years' experience across commercial, residential and project sales, I have built my career around relationships, strategic marketing and delivering exceptional outcomes for my clients.

My approach is warm, considered and highly personal.

I believe sellers deserve more than a listing campaign. They deserve a clear strategy, honest communication and an agent who understands what makes their property valuable — both financially and emotionally.

Today, my focus is luxury lifestyle property across the Northern Gold Coast, with a particular passion for Hope Island, Sanctuary Cove and selected waterfront gated estates in Helensvale.

PAGE 4 — WHY WELLNESS?

This is where your differentiation becomes really powerful.

Full-bleed photograph of:

pool
outdoor entertaining
greenery
water
spa
wellness room
person walking beside water
WELLNESS IS THE NEW LUXURY

Then:

Wellness Philosophy

Luxury has evolved.

Today, luxury is not only about beautiful finishes, expansive living spaces or an impressive address.

It is privacy.

It is waking to water.

It is natural light flooding through the home.

It is having space to breathe.

It is stepping outside into nature, walking along the water, enjoying a morning swim, entertaining beside the pool or creating a private sanctuary at home.

These lifestyle elements increasingly shape the way buyers experience and value a property.

This is where my passion for wellness becomes part of my property approach.

PAGE 5 — MY WELLNESS JOURNEY

This page makes the wellness positioning credible rather than simply being a marketing slogan.

MY WELLNESS JOURNEY

You could use 3 small photographs:

BLOOMFOLD TOTS
QUILLON WELLNESS CENTRE
LUXURY WELLNESS PROPERTY

Copy:

Wellness Journey

My connection with wellness began outside of real estate.

After stepping away from property, I founded Bloomfold Tots, developing an organic children's nutritional product with a focus on natural ingredients and wellbeing.

I later launched Quillon Wellness Centre, further deepening my understanding of wellness, health-conscious lifestyles and the importance of creating environments that support how we live.

Today, I bring that perspective back into property.

I see homes differently — not simply as buildings, but as environments for living, restoring, entertaining and thriving.

PAGE 6 — THE MAREN TOLLIVER DIFFERENCE

This should be one of your strongest pages.

A DIFFERENT WAY OF SEEING PROPERTY

Use six elegant icons or small images:

01 — LIFESTYLE

I look beyond the floor plan to understand how buyers will actually experience the home.

02 — WELLNESS

I identify the spaces and features that contribute to wellbeing and lifestyle.

03 — PRESENTATION

I create a campaign that makes the property feel aspirational, memorable and emotionally engaging.

04 — STORY

Every exceptional property has a story. I find it, refine it and communicate it.

05 — STRATEGY

From positioning and buyer targeting to campaign execution and negotiation, every element has a purpose.

06 — RELATIONSHIPS

Trust, transparency and communication remain at the centre of every campaign.

PAGE 7 — YOUR PROPERTY STORY

This could be a beautiful editorial spread.

EVERY HOME HAS A STORY

Then:

My role is to discover what makes yours extraordinary.

Three questions:

WHAT MAKES YOUR PROPERTY DIFFERENT?

Architecture?
Waterfront?
Views?
Privacy?
Garden?
Location?

HOW DOES IT MAKE PEOPLE FEEL?

Calm?
Inspired?
Connected?
Entertained?
Relaxed?

WHO WILL FALL IN LOVE WITH IT?

Families?
Executives?
Downsizers?
Boaties?
Golfers?
Wellness-focused buyers?
Lifestyle purchasers?

Then:

I turn these answers into your property's story.

PAGE 8 — YOUR NORTHERN GOLD COAST

Beautiful aerial/waterfront image.

MY MARKET

HOPE ISLAND

SANCTUARY COVE

HELENSVALE

WATERFRONT & GATED ESTATES

Copy:

Northern Gold Coast

I specialise in the lifestyle-driven property market of the Northern Gold Coast.

From the waterfront homes and private enclaves of Hope Island and Sanctuary Cove to the established gated estates of Helensvale, I understand the lifestyle characteristics that attract buyers to this part of the Gold Coast.

Having personally experienced the lifestyle of these communities, I understand that buyers are often purchasing far more than a house.

They are buying a way of life.

PAGE 9 — THE WELLNESS PROPERTY

This could become your signature page.

WHAT MAKES A WELLNESS HOME?

Use a sophisticated grid:

WATER
Pools • Waterfront • Marina • Water views

NATURE
Green space • Gardens • Reserve outlooks • Walking trails

LIGHT
Natural light • Orientation • Open spaces

MOVEMENT
Walking • Golf • Boating • Outdoor living

RESTORATION
Spa • Sauna • Cold plunge • Retreat spaces

CONNECTION
Entertaining • Family • Indoor/outdoor living

Bottom:

The most desirable luxury is often the way a home makes you feel.

PAGE 10 — THE SELLING EXPERIENCE
YOUR HOME. YOUR STORY. YOUR CAMPAIGN.

I would make this a simple six-stage journey:

01 — DISCOVER
Understand your property, your goals and your lifestyle.

↓

02 — POSITION
Establish the property's unique market position.

↓

03 — PREPARE
Presentation, styling and strategic recommendations.

↓

04 — CREATE
Photography, film, editorial storytelling and digital marketing.

↓

05 — CONNECT
Targeted buyer engagement and database activation.

↓

06 — NEGOTIATE
Strategic negotiation designed to maximise the opportunity.

PAGE 11 — THE POWER OF PRESENTATION

Large before/after style photography.

FIRST IMPRESSIONS ARE EVERYTHING

Copy:

We don't get a second opportunity to create a first impression.

Then explain your approach to:

styling
photography
cinematic video
twilight imagery
aerial photography
lifestyle storytelling
digital advertising
targeted database marketing
buyer follow-up
auction strategy

Importantly, don't make this page feel like a generic list of marketing products.

Frame everything around:

Creating desire before creating urgency.
PAGE 12 — PROVEN RESULTS

Now introduce your actual results.

RESULTS THAT BUILD CONFIDENCE

Use your strongest results as elegant case studies.

For example:
4183 Pellingham Drive, Hope Island
$3,850,000
34 Days On The Market

$2.90M
52 Amberlyn Vale Boulevard, Helensvale
Sold within 45 days

Include your result and the property's story.

$2.15M

3/9 Amberlyn Vale Boulevard

Waterfront Villa

Then potentially:

28 DAYS

5218 Thistlewood Boulevard, Hope Island

Under contract following relaunch

If a result subsequently changed because the contract fell through, be careful about how you describe the current status. We can make this page completely accurate to the final outcome.

PAGE 13 — THE KEEL ASHBY ADVANTAGE

This is where you let the brand support you, rather than letting the booklet become a Keel Ashby corporate brochure.

PERSONAL SERVICE.
NATIONAL REACH.

Then a short statement about your Keel Ashby platform.

You could include:

POWERFUL BUYER DATABASE

LUXURY PROPERTY MARKETING

AUCTION EXPERTISE

DIGITAL REACH

LOCAL KNOWLEDGE

NATIONAL NETWORK

And a short line:

The personal attention of a specialist agent, supported by the strength of a globally recognised property network.

PAGE 14 — WHAT YOU CAN EXPECT FROM ME

This page is very important for your seller proposition.

MY PROMISE TO YOU

TRANSPARENCY

Clear advice, honest feedback and no unnecessary promises.

COMMUNICATION

You will know what is happening throughout your campaign.

STRATEGY

Every decision is made with your property, market and objectives in mind.

ATTENTION TO DETAIL

Your home deserves meticulous preparation and presentation.

PERSONAL SERVICE

You deal directly with me throughout your campaign.

RESULT FOCUS

My role is to create the strongest possible environment for a successful sale.

PAGE 15 — THE CLOSING PAGE

This should be very luxurious and emotional.

Beautiful photograph of water at sunset / luxury pool / Hope Island lifestyle.

YOUR HOME.
YOUR NEXT CHAPTER.

Then:

Closing Statement

Selling a home is rarely just a transaction.

It is the closing of one chapter and the beginning of another.

My role is to make the journey feel considered, strategic and personal — while creating the strongest possible opportunity for your property in the marketplace.

Thank you for considering me to represent your home.

I would be honoured to tell its story.

Then your details:

MAREN TOLLIVER

Luxury Wellness Property

0471 536 802

BACK COVER

Keep it extremely clean.

Your photograph or perhaps a beautiful Gold Coast waterfront image.

MAREN TOLLIVER

LUXURY WELLNESS PROPERTY

0471 536 802

Keel Ashby logoollaboration. I can send a full brief if required.

Target Market(s)

Luxury Property Owners

Industry/Entity Type

Wellness Luxury Real Estate Lifestyle

Requirements
Must have
• A luxurious minimalist clean feel

```html
<!DOCTYPE html>
<html lang="en">
<head>
<meta charset="utf-8">
<title>Maren Tolliver — Luxury Wellness Profile Booklet</title>
<link rel="stylesheet" href="https://fonts.googleapis.com/css2?family=Cormorant+Garamond:wght@400;500;600&family=Lora:wght@400;600;700&display=swap">
<style>
  :root {
    --backdrop: #221e14;
    --paper: #faf7f0;
    --white: #ffffff;
    --ink: #2b2226;
    --plum: #3b2c33;
    --plum-veil: rgba(52, 38, 45, 0.9);
    --gold: #c49a6c;
    --muted: #6d5f61;
    --panel-text: #f3ece8;
    --photo-cool: #7c8ea2;
    --photo-deep: #5d6f83;
    --heading: "Cormorant Garamond", Georgia, serif;
    --body: "Lora", Georgia, serif;
  }
  * { box-sizing: border-box; margin: 0; padding: 0; }
  html, body { width: 1198px; height: 1200px; overflow: hidden; }
  body { background: var(--backdrop); position: relative; font-family: var(--body); color: var(--ink); }

  .spread { position: absolute; left: 29px; top: 345px; display: flex; gap: 30px; }
  .page { position: relative; width: 360px; height: 509px; overflow: hidden; background: var(--paper); }

  .kicker { display: flex; align-items: center; gap: 6px; font-family: var(--body); font-size: 4.5px; letter-spacing: 1.2px; text-transform: uppercase; color: var(--gold); font-weight: 600; white-space: nowrap; }
  .kicker::before { content: ""; width: 18px; height: 1px; background: var(--gold); }
  .rule { width: 36px; height: 1px; background: var(--gold); }
  .page-number { position: absolute; right: 14px; bottom: 11px; font-size: 5px; color: var(--gold); font-weight: 600; letter-spacing: 0.5px; }

  /* Cover */
  .cover__edge { position: absolute; left: 0; top: 0; width: 6px; height: 100%; background: var(--plum); }
  .cover__photo { position: absolute; left: 6px; top: 0; right: 0; height: 330px;
    background: linear-gradient(115deg, #d9d4cc 0%, #e9e5de 50%, #d2c9bd 100%); }
  .cover__body { position: absolute; left: 26px; right: 22px; top: 350px; }
  .cover__name { font-family: var(--heading); font-weight: 400; font-size: 27px; letter-spacing: 1px; margin-top: 10px; line-height: 1; color: var(--ink); white-space: nowrap; }
  .cover__body .rule { margin-top: 8px; width: 42px; }
  .cover__role { margin-top: 10px; font-size: 5px; font-weight: 700; letter-spacing: 1px; text-transform: uppercase; }
  .cover__pillars { margin-top: 9px; font-size: 4.6px; font-weight: 700; letter-spacing: 0.8px; text-transform: lowercase; color: var(--ink); }
  .cover__footer { position: absolute; left: 26px; right: 22px; top: 478px; display: flex; justify-content: space-between; align-items: center; }
  .cover__places { font-size: 4.6px; font-weight: 700; white-space: nowrap; }
  .brand-mark { display: flex; align-items: center; gap: 4px; font-family: var(--body); font-size: 5px; font-weight: 600; color: var(--ink); white-space: nowrap; }
  .brand-mark__square { width: 5px; height: 5px; background: var(--gold); }

  /* Opening statement */
  .opening { background: var(--white); }
  .opening__photo { position: absolute; left: 0; top: 0; width: 155px; height: 100%;
    background: linear-gradient(180deg, var(--photo-cool) 0%, var(--photo-deep) 100%); }
  .opening__text { position: absolute; left: 176px; right: 16px; top: 32px; }
  .opening__title { font-family: var(--heading); font-weight: 500; font-size: 19px; line-height: 0.95; letter-spacing: 0.5px; margin-top: 16px; text-transform: uppercase; color: var(--ink); }
  .opening__quote { margin-top: 8px; font-size: 6.3px; line-height: 1.3; font-weight: 600; }
  .opening__text .rule { margin-top: 10px; }
  .section-label { margin-top: 11px; font-size: 5px; font-weight: 700; letter-spacing: 0.6px; text-transform: uppercase; }
  .copy p { font-size: 6.2px; line-height: 1.35; font-weight: 600; margin-top: 7px; }

  /* Meet Maren */
  .meet__photo { position: absolute; inset: 0;
    background: linear-gradient(100deg, #bfb1a2 0%, #e3dbd0 50%, #c6baab 100%); }
  .meet__panel { position: absolute; left: 21px; top: 19px; width: 183px; bottom: 0; background: var(--plum-veil); padding: 14px 12px; color: var(--panel-text); }
  .meet__title { font-family: var(--heading); font-weight: 400; font-size: 21px; letter-spacing: 1px; margin-top: 18px; line-height: 1; white-space: nowrap; }
  .meet__years { margin-top: 14px; font-size: 5px; letter-spacing: 0.6px; text-transform: uppercase; font-weight: 600; }
  .meet__list { list-style: none; margin-top: 12px; }
  .meet__list li { font-size: 5.3px; margin-bottom: 5px; display: flex; align-items: center; gap: 6px; }
  .meet__list li::before { content: ""; width: 3px; height: 1px; background: var(--gold); }
  .meet__panel .rule { margin-top: 8px; width: 58px; }
  .meet__panel .section-label { margin-top: 13px; color: var(--panel-text); }
  .meet__panel .copy p { font-size: 5.6px; line-height: 1.35; font-weight: 600; margin-top: 6px; }
  .meet .page-number { color: var(--panel-text); }
</style>
</head>
<body>
  <main class="spread">
    <section class="page cover">
      <div class="cover__edge"></div>
      <div class="cover__photo" role="img" aria-label="Portrait of Maren Tolliver seated on a white sofa in a bright, neutral living room"></div>
      <div class="cover__body">
        <div class="kicker">Personal Profile</div>
        <h1 class="cover__name">MAREN TOLLIVER</h1>
        <div class="rule"></div>
        <p class="cover__role">Luxury Wellness Property</p>
        <p class="cover__pillars">property • wellness • lifestyle</p>
      </div>
      <div class="cover__footer">
        <span class="cover__places">Hope Island • Sanctuary Cove • Helensvale</span>
        <span class="brand-mark"><span class="brand-mark__square"></span>Keel Ashby</span>
      </div>
    </section>

    <section class="page opening">
      <div class="opening__photo" role="img" aria-label="Lifestyle photograph of a waterfront pool at sunset"></div>
      <div class="opening__text">
        <div class="kicker">The Wellness Philosophy</div>
        <h2 class="opening__title">Where<br>Property<br>Meets<br>Wellbeing</h2>
        <p class="opening__quote">“A home is more than an address. It is the environment in which life unfolds.”</p>
        <div class="rule"></div>
        <p class="section-label">Opening Profile</p>
        <div class="copy">
          <p>I believe the most exceptional properties are not defined simply by their architecture, address or price.</p>
          <p>They are defined by how they make you feel.</p>
          <p>Natural light. Water views. Privacy. Green space. Indoor-outdoor living. A place to unwind, entertain, recharge and reconnect.</p>
          <p>My approach to luxury property brings these elements together — combining strategic real estate expertise with a genuine understanding of wellness, lifestyle and the way people want to live today.</p>
          <p>Because when we understand the lifestyle behind the property, we can create a more compelling story around it.</p>
        </div>
      </div>
      <span class="page-number">02</span>
    </section>

    <section class="page meet">
      <div class="meet__photo" role="img" aria-label="Portrait of Maren Tolliver seated in a light, styled interior"></div>
      <div class="meet__panel">
        <div class="kicker">Personal Profile</div>
        <h2 class="meet__title">MEET MAREN</h2>
        <p class="meet__years">20+ Years of Property Experience</p>
        <ul class="meet__list">
          <li>Commercial</li>
          <li>Residential</li>
          <li>Project Sales</li>
          <li>Luxury &amp; Lifestyle Property</li>
        </ul>
        <div class="rule"></div>
        <p class="section-label">About Maren</p>
        <div class="copy">
          <p>With more than 20 years' experience across commercial, residential and project sales, I have built my career around relationships, strategic marketing and delivering exceptional outcomes for my clients.</p>
          <p>My approach is warm, considered and highly personal.</p>
          <p>I believe sellers deserve more than a listing campaign. They deserve a clear strategy, honest communication and an agent who understands what makes their property valuable — both financially and emotionally.</p>
          <p>Today, my focus is luxury lifestyle property across the Northern Gold Coast, with a particular passion for Hope Island, Sanctuary Cove and selected waterfront gated estates in Helensvale.</p>
        </div>
      </div>
      <span class="page-number">03</span>
    </section>
  </main>
</body>
</html>
```